Flyer Design

I will be hosting an event at Penrith's amber lantern. Here is a link to their page http://www.theamberlantern.com.au/events-and-workshops/whats-on-penrith/. I have attached the details of my course from their website below. I hope this is of some valuable assistance.

Florist and lover of all things gorgeous, Molly Hartwell from Molly Hartwell Flowers will be running this beautiful and fun workshop. Come along to learn how to make your very own floral crown. All you need to bring are some closed in shoes, an apron and an open mind ready for creativity!

Teens & adults welcome

Date 1: Saturday 11 April 2015
Time 1: 11:00-2:00pm

Date 2: Thursday 23 April 2015
Time 2: 6:00-9:00pm

Cost: $90 per person (includes materials provided – see list below)
Place: The Amber Lantern, Unit 3, 27 Baxter Lane Penrith
RSVP: Molly via email mollyhartwellflowers@fernmail.example or phone 0431 795 206

Materials provided:
• Florist scissors
• Parafilm
• Wire
• Flowers
• light snacks & refreshments

```html
<!DOCTYPE html>
<html lang="en">
<head>
<meta charset="utf-8">
<title>Floral Crowns Workshop – The Amber Lantern</title>
<link rel="stylesheet" href="https://fonts.googleapis.com/css2?family=Source+Sans+3:wght@400;600;700&family=Sofia&display=swap">
<style>
  :root {
    --page-bg: #e9e7e4;
    --paper: #ffffff;
    --sky: #8fd3e0;
    --teal: #47c3cc;
    --pink: #e8307f;
    --plum: #b07bb8;
    --lavender: #9d9cc8;
    --ink: #2d2d2d;
    --white: #ffffff;
    --rose-light: #f7dce3;
    --rose-mid: #eeb3c3;
    --rose-deep: #de8ea6;
  }
  * { margin: 0; padding: 0; box-sizing: border-box; }
  html, body { width: 914px; height: 1200px; overflow: hidden; }
  body {
    background: var(--page-bg);
    font-family: "Source Sans 3", "Myriad Pro", Arial, sans-serif;
    position: relative;
  }
  .flyer {
    position: absolute;
    left: 85px; top: 80px;
    width: 738px; height: 1040px;
    background: var(--paper);
    overflow: hidden;
    box-shadow: 0 2px 10px rgba(0,0,0,.18);
  }
  .flyer > * { position: absolute; }
  .rose-photo {
    left: 0; top: 0; width: 387px; height: 1040px;
    background:
      radial-gradient(circle at 30% 20%, var(--rose-light), transparent 45%),
      radial-gradient(circle at 45% 55%, var(--rose-mid), transparent 50%),
      radial-gradient(circle at 60% 90%, var(--rose-light), transparent 45%),
      linear-gradient(160deg, var(--rose-mid), var(--rose-deep) 60%, var(--rose-mid));
  }
  .teal-panel { left: 387px; top: 232px; width: 351px; height: 808px; background: var(--teal); }
  .shapes { left: 0; top: 0; width: 738px; height: 1040px; }

  .brand {
    left: 440px; top: 48px;
    display: flex; align-items: flex-start; gap: 14px;
  }
  .brand-mark { width: 86px; height: 86px; background: var(--pink); margin-top: 6px; }
  .brand-name {
    font-size: 34px; line-height: 30px; color: var(--ink); font-weight: 400;
  }

  .title {
    left: 400px; top: 188px; width: 330px;
    font-family: "Sofia", cursive;
    font-weight: 400;
  }
  .title-line1 { display: block; color: var(--pink); font-size: 42px; line-height: 52px; text-align: right; }
  .title-line2 { display: block; color: var(--white); font-size: 42px; line-height: 52px; text-align: right; padding-right: 4px; }

  .intro {
    left: 407px; top: 312px; width: 322px;
    font-size: 16px; line-height: 20.6px; color: var(--ink);
  }
  .intro strong { font-weight: 700; }
  .welcome { left: 455px; top: 493px; font-size: 16px; color: var(--ink); }

  .rule { left: 400px; width: 325px; height: 1px; background: var(--white); }
  .rule-top { top: 546px; }
  .rule-bottom { top: 689px; }

  .sessions {
    left: 400px; top: 566px; width: 310px;
    text-align: center; color: var(--white);
    font-size: 16px; font-weight: 700; line-height: 21px;
  }
  .sessions p + p { margin-top: 19px; }

  .cost { left: 413px; top: 730px; color: var(--ink); font-size: 16px; }
  .cost-price { display: block; color: var(--pink); font-size: 23px; font-weight: 700; line-height: 28px; }

  .materials {
    left: 415px; top: 780px; color: var(--white);
    font-size: 20.5px; line-height: 27.3px;
  }
  .materials ul { list-style: none; }
  .materials li::before { content: "• "; }

  .rsvp {
    left: 0; top: 627px; width: 380px; height: 121px;
    background: var(--plum); color: var(--white);
    text-align: center; padding: 5px 0 0 20px;
  }
  .rsvp-tip {
    left: 0; top: 627px; width: 0; height: 0;
    border-top: 40px solid transparent;
    border-bottom: 40px solid transparent;
    border-left: 40px solid var(--pink);
  }
  .rsvp h3 { font-size: 19px; font-weight: 700; letter-spacing: .5px; line-height: 20px; }
  .rsvp p { font-size: 16px; line-height: 21px; }
  .rsvp .place { font-size: 14.5px; font-weight: 700; }
</style>
</head>
<body>
  <main class="flyer">
    <div class="rose-photo" role="img" aria-label="Close-up photograph of soft pink roses with water droplets"></div>
    <div class="teal-panel"></div>

    <svg class="shapes" viewBox="0 0 738 1040" aria-hidden="true">
      <polygon points="0,0 738,0 738,18 0,62" fill="var(--sky)"/>
      <polygon points="387,18 738,18 738,232 387,232" fill="var(--paper)"/>
      <polygon points="0,1036 738,975 738,1040 0,1040" fill="var(--lavender)" opacity=".9"/>
    </svg>

    <div class="brand">
      <span class="brand-mark"></span>
      <span class="brand-name">the<br>amber<br>lantern</span>
    </div>

    <h1 class="title">
      <span class="title-line1">Floral Crowns</span>
      <span class="title-line2">Workshop</span>
    </h1>

    <p class="intro">Florist and lover of all things gorgeous, Molly Hartwell from <strong>Molly Hartwell Flowers</strong> will be running this beautiful and fun workshop.<br>Come along to learn how to make your very own floral crown. All you need to bring are some closed in shoes, an apron and an open mind ready for creativity!</p>
    <p class="welcome">Teens &amp; Adults Welcome</p>

    <div class="rule rule-top"></div>
    <div class="sessions">
      <p>Date 1: Saturday 11 April 2015<br>Time 1: 11:00-2:00pm</p>
      <p>Date 2: Thursday 23 April 2015<br>Time 2: 6:00-9:00pm</p>
    </div>
    <div class="rule rule-bottom"></div>

    <p class="cost"><span class="cost-price">Cost: $90 per person</span>(includes materials provided)</p>

    <div class="materials">
      <p>Materials provided:</p>
      <ul>
        <li>Florist scissors</li>
        <li>Parafilm</li>
        <li>Wire</li>
        <li>Flowers</li>
        <li>light snacks &amp; refreshments</li>
      </ul>
    </div>

    <section class="rsvp">
      <h3>RSVP:</h3>
      <p>Molly via email mollyhartwellflowers@fernmail.example<br>or phone 0431 795 206</p>
      <h3>PLACE:</h3>
      <p class="place">The Amber Lantern, Unit 3, 27 Baxter Lane Penrith</p>
    </section>
    <div class="rsvp-tip"></div>
  </main>
</body>
</html>
```